Sudden Tides "Lantern Road" New Single Cover

Create cover artwork for the band Sudden Tides' new single "Lantern Road" being released early 2020. Style, font and graphics to be consistent with band's previous releases and overall brand identity. Visit www.suddentidesband.example and our Spotify page https://music.example.net/artist/7QzWpLx3RtVnKd8e2YbHcJ?si=MUrTgKa4PLe7skvWq2AmZd to view our previous releases and overall brand identity. Some examples attached as well. We are looking for someone to work with on future projects as well.

Lyrics are here: https://docs.example.org/document/d/3KTp9wrn_2ZQa8eXb4Lo_fimH7C5m83Jz4Pd70hrtVcA/edit

Music is here: https://audiostream.example.com/suddentides/lantern-road/s-pzkwa

Font styles to use
Sans Serif

Colors

Designer to choose colors to be used in the design.

Requirements
Must have
• Must be consistent with current brand identity and with prior album / single art.

```html
<!DOCTYPE html>
<html lang="en">
<head>
<meta charset="utf-8">
<title>Sudden Tides – Lantern Road</title>
<link rel="stylesheet" href="https://fonts.googleapis.com/css2?family=Montserrat:wght@500;800&display=swap">
<style>
  :root {
    --amber: #f5b01e;
    --teal: #22a89c;
    --title-yellow: #f9b21f;
    --navy: #1f2a5a;
  }
  html, body {
    margin: 0;
    padding: 0;
    width: 1200px;
    height: 1200px;
    overflow: hidden;
  }
  .cover {
    position: relative;
    width: 1200px;
    height: 1200px;
    background: linear-gradient(to right, var(--amber) 0%, #b6ad5e 45%, var(--teal) 100%);
    font-family: "Montserrat", sans-serif;
    overflow: hidden;
  }
  .single-title {
    position: absolute;
    left: 510px;
    top: 18px;
    margin: 0;
    font-weight: 800;
    font-size: 190px;
    line-height: 294px;
    letter-spacing: -4px;
    color: var(--title-yellow);
    text-shadow: -36px 26px 0 var(--navy);
  }
  .single-title .line {
    display: block;
    white-space: nowrap;
  }
  .band-name {
    position: absolute;
    left: 128px;
    top: 958px;
    margin: 0;
    font-weight: 500;
    font-size: 50px;
    line-height: 60px;
    letter-spacing: 9px;
    color: var(--navy);
    text-transform: uppercase;
  }
  .band-name .line {
    display: block;
    white-space: nowrap;
  }
</style>
</head>
<body>
  <main class="cover">
    <h1 class="single-title" aria-label="Lantern Road"><span class="line">LAN</span><span class="line">TERN</span><span class="line">ROAD</span></h1>
    <p class="band-name" aria-label="Sudden Tides"><span class="line">Sudden</span><span class="line">Tides</span></p>
  </main>
</body>
</html>
```